Redesign specialty cleaning services business brochure

I need a brochure re-designed and updated to reflect packages we sell for starting your own specialty cleaning business. We are a specialty cleaning company that has been in business for over 35 years and our company literature needs an update.The brochure needs to be a downloadable file as well as print-ready.The download will go on 2 of our websites https://dovrantco.com/ and http://tarvelbrookpolishinstitute.com/. I will attach the brochure that needs to be redesigned. They have not been updated for several years. I have new images to add to the updated brochure.
Colors
Designer to choose colors to be used in the design.
Look and feel
Each slider illustrates characteristics of the customer's brand and the style your logo design should communicate.

```html
<!DOCTYPE html>
<html lang="en">
<head>
<meta charset="utf-8">
<title>Window Cleaning Startup Packages</title>
<link rel="stylesheet" href="https://fonts.googleapis.com/css2?family=Montserrat:wght@500;700;800&family=EB+Garamond&display=swap">
<style>
:root{
  --page-top:#b3ddf3;
  --page-bottom:#e6f3fa;
  --sky:#7b9fe2;
  --sky-deep:#5b7fc8;
  --teal:#4eaacb;
  --green:#07893a;
  --green-text:#0a8a3a;
  --navy:#364a63;
  --orange:#f7941d;
  --ink:#2b2f36;
  --white:#ffffff;
}
*{margin:0;padding:0;box-sizing:border-box}
html,body{width:848px;height:1200px;overflow:hidden}
body{
  background:linear-gradient(180deg,var(--page-top),var(--page-bottom));
  font-family:"Montserrat",sans-serif;
  position:relative;
}
.flyer{
  position:absolute;left:110px;width:629px;height:469px;
  overflow:hidden;box-shadow:0 6px 14px rgba(40,60,90,.35);
}
.flyer--rxt{top:113px}
.flyer--dlv{top:639px}
.flyer__backdrop{
  position:absolute;inset:0;
  background:
    linear-gradient(160deg,rgba(40,50,70,0) 0 38%,rgba(50,60,80,.55) 40% 45%,rgba(40,50,70,0) 47%),
    linear-gradient(180deg,var(--sky) 0%,#8fb0e8 45%,var(--sky-deep) 100%);
}
.flyer__title{position:absolute;left:26px;top:33px;color:var(--white);font-weight:800;line-height:1}
.flyer__title .kicker{display:block;font-size:18.5px;font-weight:700}
.flyer__title .line{display:block;font-size:25px;margin-top:2px;letter-spacing:.2px}
.flyer__title .big{display:block;font-size:36px;margin-top:-1px}
.photo{position:absolute;border:2.5px solid var(--white)}
.teal-frame{position:absolute;background:var(--teal)}
.url-band{
  position:absolute;left:0;width:337px;height:31px;background:var(--green);
  color:var(--white);font-weight:700;font-size:13.4px;
  display:flex;align-items:center;justify-content:center;
}
.footer-band{position:absolute;left:0;right:0;bottom:0;background:var(--navy)}
.contact{position:absolute;left:0;width:320px;text-align:center;color:var(--white)}
.contact__name{color:var(--orange);font-weight:800;font-size:14px;margin-bottom:4px}
.contact__line{font-size:7.6px;font-weight:500;line-height:10px}
.tagline{
  position:absolute;left:337px;width:268px;text-align:center;
  font-family:"EB Garamond",serif;color:var(--orange);font-size:11px;
}
.offer{
  position:absolute;left:337px;top:33px;width:268px;height:402px;border-radius:12px;overflow:hidden;
  background:linear-gradient(180deg,rgba(255,255,255,.95),rgba(225,228,233,.95));
}
.offer__head{
  background:var(--green);color:var(--white);text-align:center;height:82px;padding-top:8px;
}
.offer__lead{font-weight:800;font-size:11px;line-height:14px}
.offer__price{font-weight:500;font-size:10.5px;line-height:13px;margin-top:2px}
.offer__note{font-size:5.5px;margin-top:3px}
.offer__body{padding:10px 0 0 17px;color:var(--ink)}
.offer__intro{color:var(--green-text);font-weight:800;font-size:11px;margin-bottom:4px}
.offer__group{color:var(--green-text);font-weight:700;font-size:9.6px;margin-top:8px}
.offer__group:first-of-type{margin-top:0}
.offer__list{list-style:none;font-size:7.8px;line-height:11.3px;padding-left:0}
.offer__list li::before{content:"•";margin-right:4px}
.flyer--dlv .offer__list{line-height:12.8px}
.flyer--dlv .offer__group{margin-top:7px}
</style>
</head>
<body>

<section class="flyer flyer--rxt">
  <div class="flyer__backdrop" role="img" aria-label="Close-up of a soapy window pane with squeegee under a blue sky"></div>
  <h1 class="flyer__title"><span class="kicker">THE “RXT”</span><span class="line">WINDOW CLEANING</span><span class="big">PACKAGE</span></h1>
  <div class="teal-frame" style="left:10px;top:126px;width:296px;height:250px"></div>
  <div class="photo" style="left:24px;top:139px;width:90px;height:108px;background:linear-gradient(160deg,#6d7f95,#2f3f58)" role="img" aria-label="Technician cleaning a storefront window with a pole"></div>
  <div class="photo" style="left:111px;top:139px;width:90px;height:108px;background:linear-gradient(160deg,#c9ccd0,#7c8590)" role="img" aria-label="Technician squeegeeing a glass door"></div>
  <div class="photo" style="left:198px;top:139px;width:95px;height:108px;background:linear-gradient(160deg,#8b8f95,#3b4558)" role="img" aria-label="Technician carrying a sectional ladder"></div>
  <div class="photo" style="left:24px;top:259px;width:90px;height:108px;background:linear-gradient(160deg,#c8414a,#8c2a33)" role="img" aria-label="Mini-blind cleaning rack in yellow and blue"></div>
  <div class="photo" style="left:111px;top:259px;width:90px;height:108px;background:linear-gradient(160deg,#a9a49b,#5f5c58)" role="img" aria-label="Technician washing hung mini-blinds"></div>
  <div class="photo" style="left:198px;top:259px;width:95px;height:108px;background:linear-gradient(160deg,#c9b9ab,#8d8680)" role="img" aria-label="Racks of cleaned mini-blinds indoors"></div>
  <div class="url-band" style="top:376px">www.TarvelbrookPolishInstitute.com</div>
  <div class="footer-band" style="height:62px"></div>
  <div class="contact" style="top:413px"><p class="contact__name">Dorian Vale</p><p class="contact__line">2218 Harrow Creek Rd Ste 40, Larkmont Ca. 95012</p><p class="contact__line">Ph. 877-555-0162 &nbsp;|&nbsp; Fax. 877-555-0179 &nbsp;|&nbsp; dovrant.desk@mailbox.com</p></div>
  <div class="offer">
    <div class="offer__head">
      <p class="offer__lead">The “RXT”Startup Package is a complete<br>7 day Window Cleaning System</p>
      <p class="offer__price">Includes Training and Equipment<br>for Just $19,995.00</p>
      <p class="offer__note">(Training Up To 3 Team Members)</p>
    </div>
    <div class="offer__body">
      <p class="offer__intro">HERE IS JUST SOME OF WHAT YOU GET:</p>
      <h3 class="offer__group">Hands on Window Cleaning Training</h3>
      <ul class="offer__list"><li>Beginning &amp; Advance Window Cleaning Training</li><li>Power Washing Training</li><li>Mini-Blind Cleaning Training</li><li>Ladder Safety Training Techniques</li><li>Bidding &amp; Estimating Techniques</li></ul>
      <h3 class="offer__group">Equipment Includes</h3>
      <ul class="offer__list"><li>1 Complete Window Cleaning Bucket &amp; Tool Setup</li><li>4 1/2 Piece Sectional Window Cleaning Ladder Set</li><li>The BlindSwift Kit Mobile Mini-Blind Cleaning System</li><li>3 Quick Connect Water Keys</li></ul>
      <h3 class="offer__group">Company Branding Includes</h3>
      <ul class="offer__list"><li>4 Page Website with 6 Months Free Hosting</li><li>1 Logo Deign</li><li>5000 Door Hangers</li><li>12 Uniform Shirts and Hats with Logo</li><li>2 (17.3”x11.25”) Magnetic Vehicle Signs</li><li>1 Designed Letterhead, Business Card &amp; Brochure</li></ul>
      <h3 class="offer__group">Office Set-up</h3>
      <ul class="offer__list"><li>Overview of LedgerPro Software Application</li><li>Overview of Forms Needed for Business Operation</li><li>Window Cleaning Marketing &amp; Internet Advertising Plan</li></ul>
    </div>
  </div>
  <p class="tagline" style="top:441px">Clear Skills for Every Pane!</p>
</section>

<section class="flyer flyer--dlv">
  <div class="flyer__backdrop" role="img" aria-label="Close-up of a soapy window pane with squeegee under a blue sky"></div>
  <h1 class="flyer__title"><span class="kicker">THE “DLV”</span><span class="line">WINDOW CLEANING</span><span class="big">PACKAGE</span></h1>
  <svg style="position:absolute;left:0;top:0" width="629" height="469" aria-hidden="true">
    <polygon fill="#4eaacb" points="24,132 173,132 173,202 216,202 216,254 295,254 295,353 145,353 145,299 66,299 66,242 24,242"/>
  </svg>
  <div class="photo" style="left:34px;top:140px;width:130px;height:68px;border:none;background:linear-gradient(160deg,#e8ecef,#b9c3cc)" role="img" aria-label="Cleaner wiping a window with yellow gloves"></div>
  <div class="photo" style="left:77px;top:208px;width:130px;height:84px;border:none;background:linear-gradient(160deg,#9aa3ad,#4c5560)" role="img" aria-label="Technician on a ladder cleaning upper windows"></div>
  <div class="photo" style="left:156px;top:262px;width:129px;height:82px;border:none;background:linear-gradient(160deg,#e1c9b4,#8d7666)" role="img" aria-label="Technician washing windows at sunset"></div>
  <div class="url-band" style="top:369px">www.TarvelbrookPolishInstitute.com</div>
  <div class="footer-band" style="height:69px"></div>
  <div class="contact" style="top:411px"><p class="contact__name">Dorian Vale</p><p class="contact__line">2218 Harrow Creek Rd Ste 40, Larkmont Ca. 95012</p><p class="contact__line">Ph. 877-555-0162 &nbsp;|&nbsp; Fax. 877-555-0179 &nbsp;|&nbsp; dovrant.desk@mailbox.com</p></div>
  <div class="offer">
    <div class="offer__head">
      <p class="offer__lead">The “DLV”Startup Package is a complete<br>3 day Window Cleaning System</p>
      <p class="offer__price">Includes Training and Equipment<br>for Just $9,995.00</p>
      <p class="offer__note">(Training Up To 2 Team Members)</p>
    </div>
    <div class="offer__body">
      <p class="offer__intro">HERE IS JUST SOME OF WHAT YOU GET:</p>
      <h3 class="offer__group">Hands-on Window Cleaning Training</h3>
      <ul class="offer__list"><li>Basic Hands on Window Cleaning Training</li><li>Ladder Safety Training Techniques</li><li>Bidding &amp; Estimating Techniques</li></ul>
      <h3 class="offer__group">Equipment Includes</h3>
      <ul class="offer__list"><li>1 Complete Window Cleaning Bucket &amp; Tool Setup</li><li>4 1/2 Piece Sectional Window Cleaning Ladder Set</li></ul>
      <h3 class="offer__group">Company Branding Includes</h3>
      <ul class="offer__list"><li>3 Page Website with 6 Months Free Hosting</li><li>1 Logo Deign</li><li>2500 Door Hangers</li><li>6 Uniform Shirts and Hats with Logo</li><li>2 (17.3”x11.25”) Magnetic Vehicle Signs</li><li>1 Designed Letterhead, Business Card &amp; Brochure</li></ul>
      <h3 class="offer__group">Office Set-up</h3>
      <ul class="offer__list"><li>20 hours of Business Consulting</li><li>Window Cleaning Marketing &amp; Internet Advertising Plan</li></ul>
    </div>
  </div>
  <p class="tagline" style="top:441px">Clear Skills for Every Pane!</p>
</section>

</body>
</html>
```